Secret agents need a new website

We organize child birthdays with a special agents in london & Bristol.

Current design does not grab people attention, and they leave website too soon.

Colors. Up to 3 main colors, but maybe black + green + white, or blact + red + white, would suit our secret operations website.

Current website:
www.moonjumble.co.uk

Dear designers, thanks very much for working on our design.

Please try to make like a SPECIAL YOUNG AGENT TRAINING WEBSITE, all other
entertainers have childish websites, and we want to differentiate from them.

Not sure if it helps, but I like this design very much:

Guys,

I am looking for spy/secret agent/action themed design. You submitting awesome designs, and if I have another business, I just choose any of them at it would be perfect. But I want spy/secret agent/action themed.

Please feel free to add elements like:

1. Yellow, or RED line CRIME SCENE DO NOT CROSS
2. Some words or phrases can be black background - white text. 
3. Some stamps like this:
http://www.plenvoria.com/pic-48120957/stock-vector-assorted-office-ink-marks-classified-private-etc.html?src=qTm4Lo-bRwNxZ3e-p81KcE-1-16

4.spy guys http://www.plenvoria.com/pic-39418275/stock-vector-sleuth-in-long-overcoat-vintage-clip-art.html?src=hdWpRmTeQoXs4v9bnaLjCf-1-9

Do not make too much elements, I like simple designs, less details.  

PLEASE NO CHILDS WITH GUNS, and better NO GUNS at all. 

Target Market(s)

Audience: Woman, but should look cool for kids too.
(Please DO NOT make design childish)

Requirements
Must have
• Please take a look at current website
• 1. Texts should be easy to read and not too small.
• 2. White/bright background
• 3. Lead form should stay on page
• 4. Header, and footer should be not too big.
• 5. Infographic is not needed
• Extra elements
• 1. Company blog
• 2. Client zone
• 3. Venue finder
• 4. How to pay deposit
Nice to have
• We accept
• Quidlo
• marrowfeld
• (please browse logos)
• On header would be better to use
• MoonJumble.co.uk
• But also add somethere, in association with Fen-rally.co.uk.
• Please use logo with .co.uk
• In archive you will find without background if needed too.

```html
<!DOCTYPE html>
<html lang="en">
<head>
<meta charset="utf-8">
<title>Fen-rally.co.uk – Spy Birthday Parties</title>
<link href="https://fonts.googleapis.com/css2?family=Nunito:wght@700;800;900&family=Arvo:wght@700&family=Satisfy&family=Arimo:wght@400;700&display=swap" rel="stylesheet">
<style>
:root{
  --sky:#a9dcdf;
  --sky-deep:#8fcdd1;
  --panel:#eaf7f7;
  --white:#ffffff;
  --green:#6cb31e;
  --green-light:#8fcf3c;
  --green-dark:#4f8f12;
  --ink:#2b2b2b;
  --grey:#4a4a4a;
  --muted:#6f7a7a;
  --charcoal:#2a2a2a;
  --charcoal-2:#1c1c1c;
  --line:#dcdcdc;
}
*{margin:0;padding:0;box-sizing:border-box}
html,body{width:719px;height:1200px;overflow:hidden}
body{background:var(--sky);font-family:"Arimo",Arial,sans-serif;color:var(--ink);position:relative}
.abs{position:absolute}
.slab{font-family:"Arvo",Georgia,serif;font-weight:700}
.round{font-family:"Nunito",Arial,sans-serif;font-weight:900}
.script{font-family:"Satisfy",cursive;font-weight:400}

/* header */
.logo-card{left:70px;top:0;width:158px;height:86px;background:var(--white);box-shadow:0 2px 6px rgba(0,0,0,.15);transform:rotate(-2deg);display:flex;align-items:center;justify-content:center;gap:6px;z-index:3}
.logo-card .mark{width:14px;height:14px;background:var(--ink)}
.logo-card .name{font-family:"Nunito",sans-serif;font-weight:900;font-size:17px;color:var(--green)}
.call{left:400px;top:18px;display:flex;align-items:center;gap:7px}
.call .ph{width:26px;height:26px;border-radius:50%;background:var(--green);display:flex;align-items:center;justify-content:center}
.call small{display:block;font-size:9px;color:var(--grey);line-height:10px}
.call strong{display:block;font-size:15px;color:var(--grey);line-height:16px;letter-spacing:.5px}
.enquiry{left:554px;top:19px;width:93px;height:25px;background:linear-gradient(var(--green-light),var(--green));border:1px solid var(--green-dark);border-radius:2px;color:var(--white);font-size:11px;display:flex;align-items:center;justify-content:center;gap:5px}
.nav{top:58px;height:26px;display:flex;z-index:4}
.nav a{position:absolute;top:0;height:26px;background:#3d3f40;color:var(--white);font-size:10.5px;text-decoration:none;display:flex;align-items:center;justify-content:center}
.nav a.on{background:linear-gradient(var(--green-light),var(--green))}
.nav a.on::after{content:"";position:absolute;bottom:-5px;left:50%;margin-left:-5px;border:5px solid transparent;border-bottom:0;border-top-color:var(--green)}

/* hero */
.hero{left:70px;top:67px;width:580px;height:259px;background:var(--panel);box-shadow:0 1px 3px rgba(0,0,0,.1)}
.hero h1{position:absolute;left:22px;top:52px;font-size:27px;line-height:27px;color:var(--green);font-family:"Nunito",sans-serif;font-weight:900}
.hero .tag{position:absolute;left:22px;top:112px;font-size:11px;color:var(--grey)}
.hero p{position:absolute;left:22px;top:133px;width:230px;font-size:10px;line-height:12.5px;color:var(--ink)}
.btn-dark{position:absolute;left:24px;top:171px;width:111px;height:24px;background:#4b4d4e;border:1px solid #2f3031;border-radius:2px;color:var(--white);font-size:10.5px;display:flex;align-items:center;justify-content:center;gap:5px}
.dots{position:absolute;left:25px;top:212px;display:flex;gap:3px}
.dots i{width:7px;height:7px;border-radius:50%;background:var(--white);border:1px solid #ccc}
.dots i.on{background:var(--ink);border-color:var(--ink)}
.video{position:absolute;left:269px;top:48px;width:293px;height:179px;background:var(--white);padding:3px;box-shadow:0 2px 6px rgba(0,0,0,.25)}
.video .left{position:absolute;left:3px;top:3px;width:144px;height:159px;background:radial-gradient(circle at 50% 40%,#3a3a3a,#050505 70%)}
.video .right{position:absolute;left:147px;top:3px;width:143px;height:159px;background:linear-gradient(135deg,#e6e6e6,#bdbdbd)}
.video .play{position:absolute;left:124px;top:63px;width:42px;height:42px;border-radius:50%;background:radial-gradient(circle at 40% 35%,var(--green-light),var(--green-dark));border:2px solid var(--white);display:flex;align-items:center;justify-content:center}
.video .bar{position:absolute;left:3px;bottom:3px;width:287px;height:14px;background:var(--charcoal-2);display:flex;align-items:center;gap:6px;padding:0 5px;color:var(--white);font-size:6px}
.video .bar .track{flex:1;height:3px;background:#555;border-radius:2px}

/* welcome */
.welcome{left:70px;top:333px;width:580px;height:197px;background:var(--white)}
.welcome h2{position:absolute;left:20px;top:20px;font-size:16px;font-family:"Nunito",sans-serif;font-weight:900;color:var(--ink)}
.welcome .intro{position:absolute;left:20px;top:43px;width:330px;font-size:7.5px;line-height:11px;color:var(--grey)}
.step{position:absolute;top:77px;width:70px;text-align:center}
.step .c{width:60px;height:60px;margin:0 auto;border-radius:50%;background:var(--white);box-shadow:0 1px 4px rgba(0,0,0,.2);display:flex;align-items:center;justify-content:center}
.step span{display:block;margin-top:12px;font-size:7px;line-height:9px;color:var(--grey)}
.quote{position:absolute;left:392px;top:25px;width:172px;height:132px;background:#3d3f40;border-radius:3px;padding:4px}
.quote .in{width:100%;height:100%;border:1px dotted #9a9a9a;position:relative}
.quote h3{position:absolute;left:12px;top:8px;font-size:12px;color:var(--white);font-family:"Nunito",sans-serif;font-weight:800}
.quote .photo{position:absolute;left:14px;top:30px;width:52px;height:82px;background:linear-gradient(#c9a07a,#e8d2c0 55%,#f2f2f2)}
.quote q{position:absolute;left:74px;top:32px;width:86px;font-family:"Satisfy",cursive;font-size:8.5px;line-height:10px;color:#e6e6e6;quotes:none}
.quote .who{position:absolute;left:74px;top:98px;font-size:7px;color:var(--green-light);font-weight:700}
.quote .who small{display:block;color:#b5b5b5;font-weight:400;font-size:6.5px}

/* pricing */
.pricing{left:70px;top:530px;width:580px;height:332px;background:radial-gradient(ellipse at 55% 55%,#3a3a3a,var(--charcoal-2) 80%)}
.pricing h2{position:absolute;left:0;top:22px;width:580px;text-align:center;color:var(--white);font-size:24px;line-height:28px}
.pricing h2 b{font-family:"Nunito",sans-serif;font-weight:900;font-size:23px}
.card{position:absolute;top:68px;width:194px;height:215px;background:#2b2b2b;box-shadow:0 2px 6px rgba(0,0,0,.5)}
.card .head{height:54px;background:linear-gradient(var(--white),#e3e3e3);display:flex;align-items:center;justify-content:center;gap:8px}
.card .head i{width:40px;height:1px;background:#cfcfcf}
.card .head b{font-family:"Nunito",sans-serif;font-weight:900;font-size:29px;color:#3a3a3a}
.card ul{list-style:none;margin:13px 12px 0}
.card li{height:22.5px;border-bottom:1px dotted #4e4e4e;display:flex;align-items:center;gap:8px;font-size:8px;color:var(--white);padding-left:6px}
.card li:last-child{border-bottom:0}
.order{position:absolute;left:46px;top:196px;width:101px;height:27px;background:linear-gradient(var(--green-light),var(--green));border:1px solid var(--green-dark);border-radius:2px;color:var(--white);font-size:11px;display:flex;align-items:center;justify-content:center}

/* share */
.share{left:70px;top:862px;width:580px;height:140px;background:var(--panel)}
.share h2{position:absolute;left:0;top:18px;width:580px;text-align:center;font-size:20px;color:var(--green)}
.share h2 b{font-family:"Nunito",sans-serif;font-weight:900}
.soc{position:absolute;top:55px;width:50px;height:50px;border-radius:50%;background:var(--white);box-shadow:0 1px 4px rgba(0,0,0,.15);display:flex;align-items:center;justify-content:center;font-size:8px;font-weight:700;color:var(--green)}
.soc.on{background:#6b9b5a;color:var(--white)}
.top-btn{left:673px;top:953px;width:34px;height:34px;border-radius:50%;background:var(--sky-deep);display:flex;align-items:center;justify-content:center}

/* footer */
.band{left:0;top:1002px;width:719px;height:142px;background:radial-gradient(ellipse at 50% 50%,#3b3b3b,#0e0e0e 75%)}
.band h3{position:absolute;left:70px;top:44px;font-size:13px;color:var(--white)}
.band p{position:absolute;left:70px;top:72px;width:215px;font-size:8px;line-height:9.7px;color:var(--white)}
.band .agent{position:absolute;left:316px;top:22px;width:100px;height:120px;background:linear-gradient(#8a8a8a,#4d4d4d)}
.band .suit{position:absolute;left:446px;top:64px;font-size:13px;line-height:18px;color:#d8d8d8;letter-spacing:.5px}
.foot-nav{left:0;top:1155px;width:719px;display:flex;justify-content:center;gap:10px;font-size:10px;color:var(--ink);letter-spacing:.6px}
.copy{left:0;top:1173px;width:719px;text-align:center;font-size:7px;color:var(--grey)}
</style>
</head>
<body>

<header>
  <div class="abs logo-card"><i class="mark"></i><span class="name">Fen-rally.co.uk</span></div>
  <div class="abs call">
    <span class="ph"><svg width="13" height="13" viewBox="0 0 24 24"><path fill="#fff" d="M6.6 10.8a15 15 0 0 0 6.6 6.6l2.2-2.2c.3-.3.7-.4 1-.2 1.1.4 2.3.6 3.6.6.6 0 1 .4 1 1V20c0 .6-.4 1-1 1A17 17 0 0 1 3 4c0-.6.4-1 1-1h3.5c.6 0 1 .4 1 1 0 1.3.2 2.5.6 3.6.1.3 0 .7-.2 1z"/></svg></span>
    <span class="slab"><small>Call Us:</small><strong>020 4710 5583</strong></span>
  </div>
  <div class="abs enquiry slab">
    <svg width="10" height="10" viewBox="0 0 10 10"><rect x="1" y="1" width="8" height="8" fill="none" stroke="#fff" stroke-width="1.2"/><path d="M3 5l1.5 1.5L7.5 3" stroke="#fff" stroke-width="1.2" fill="none"/></svg>Enquiry
  </div>
  <nav class="abs nav slab">
    <a class="on" style="left:256px;width:48px">Home</a>
    <a style="left:308px;width:78px">Equipment</a>
    <a style="left:390px;width:68px">Invitation</a>
    <a style="left:461px;width:73px">Party bags</a>
    <a style="left:537px;width:45px">Prices</a>
    <a style="left:586px;width:64px">Contact</a>
  </nav>
</header>

<section class="abs hero">
  <h1>Capture your<br>kids imagination</h1>
  <div class="tag script">with a Spy Birthday party in London, Bristol</div>
  <p>I wanted a kids birthday party with a difference, and then I found the Top Secret Spy Party</p>
  <div class="btn-dark slab">More Info
    <svg width="10" height="9" viewBox="0 0 10 9"><path d="M0 4.5h8M5 1l3.5 3.5L5 8" stroke="#fff" stroke-width="1.6" fill="none"/></svg>
  </div>
  <div class="dots"><i></i><i style="background:var(--green);border-color:var(--green)"></i><i class="on"></i></div>
  <div class="video">
    <div class="left" role="img" aria-label="Spy school confidential emblem on black"></div>
    <div class="right" role="img" aria-label="Secret agent ID card with a young agent's photo, name and fingerprint"></div>
    <div class="play"><svg width="16" height="18" viewBox="0 0 16 18"><path d="M2 1l13 8-13 8z" fill="#fff"/></svg></div>
    <div class="bar"><span>▶</span><span>00:00</span><span class="track"></span><span>00:00</span><span>◂▮</span></div>
  </div>
</section>

<section class="abs welcome">
  <h2>Welcome to fen-rally</h2>
  <p class="intro">Every parent wants to give their child the best birthday party, but we don't always have the time to plan and prepare for an extra special birthday party with the wow factor.</p>

  <div class="step" style="left:16px"><div class="c">
    <svg width="26" height="26" viewBox="0 0 26 26"><rect x="1" y="3" width="24" height="22" rx="2" fill="#fff" stroke="#bbb"/><rect x="1" y="3" width="24" height="7" rx="2" fill="#d9312b"/><text x="13" y="22" text-anchor="middle" font-family="Arimo,sans-serif" font-weight="700" font-size="10" fill="#333">24</text></svg>
  </div><span>Choos a date<br>and time</span></div>

  <div class="step" style="left:87px"><div class="c">
    <svg width="28" height="24" viewBox="0 0 28 24"><path d="M3 11L14 2l11 9" fill="none" stroke="#555" stroke-width="2"/><rect x="6" y="10" width="16" height="12" fill="#e9e2d4" stroke="#888"/><rect x="12" y="15" width="4" height="7" fill="#7a5a3a"/><rect x="8" y="13" width="3" height="3" fill="#7fb2d6"/><rect x="17" y="13" width="3" height="3" fill="#7fb2d6"/></svg>
  </div><span>Choos Place</span></div>

  <div class="step" style="left:157px"><div class="c">
    <svg width="28" height="22" viewBox="0 0 28 22"><rect x="1" y="1" width="20" height="13" rx="2" fill="#8fc4e8"/><rect x="7" y="7" width="20" height="13" rx="2" fill="#7cc25a"/><rect x="7" y="10" width="20" height="2.5" fill="#3d7a25"/></svg>
  </div><span>Pay a deposit</span></div>

  <div class="step" style="left:228px"><div class="c">
    <svg width="28" height="22" viewBox="0 0 28 22"><rect x="2" y="5" width="22" height="15" fill="#f3ead2" stroke="#c9b98f"/><path d="M2 5l11 8 11-8" fill="none" stroke="#c9b98f"/><rect x="17" y="1" width="9" height="6" fill="#6cb31e"/></svg>
  </div><span>You will get<br>invitation by post</span></div>

  <div class="step" style="left:299px"><div class="c">
    <svg width="26" height="22" viewBox="0 0 26 22"><rect x="1" y="1" width="24" height="20" fill="#fff" stroke="#d9312b" stroke-width="2" stroke-dasharray="3 2"/><rect x="6" y="7" width="14" height="2" fill="#5a7fb8"/><rect x="6" y="12" width="10" height="2" fill="#5a7fb8"/></svg>
  </div><span>Invite quotes</span></div>

  <aside class="quote"><div class="in">
    <h3>What parents Say...</h3>
    <div class="photo" role="img" aria-label="Portrait photo of a smiling mother"></div>
    <q>We joined Tumblebee when they first started out and were a very small company. They have become a huge con-</q>
    <div class="who">Mara Lindell, Essex,<small>(mum to Ruby Lindell)</small></div>
  </div></aside>
</section>

<section class="abs pricing">
  <h2><span class="script">Lets Review</span> <b>The Pricng</b> <span class="script">First</span></h2>

  <div class="card" style="left:85px">
    <div class="head"><i></i><b>£175</b><i></i></div>
    <ul>
      <li><svg width="9" height="8" viewBox="0 0 9 8"><path d="M1 4l2.5 2.5L8 1" stroke="#8fcf3c" stroke-width="1.8" fill="none"/></svg>Entertainer Spy</li>
      <li><svg width="9" height="8" viewBox="0 0 9 8"><path d="M1 4l2.5 2.5L8 1" stroke="#8fcf3c" stroke-width="1.8" fill="none"/></svg>15 Colour Invitation</li>
      <li><svg width="9" height="8" viewBox="0 0 9 8"><path d="M1 4l2.5 2.5L8 1" stroke="#8fcf3c" stroke-width="1.8" fill="none"/></svg>12 party bags</li>
      <li><svg width="9" height="8" viewBox="0 0 9 8"><path d="M1 4l2.5 2.5L8 1" stroke="#8fcf3c" stroke-width="1.8" fill="none"/></svg>12 laminated spy ID's</li>
      <li><svg width="9" height="8" viewBox="0 0 9 8"><path d="M1 4l2.5 2.5L8 1" stroke="#8fcf3c" stroke-width="1.8" fill="none"/></svg>2 hours + fun guaranteed</li>
    </ul>
    <div class="order slab">Order Now</div>
  </div>

  <div class="card" style="left:300px">
    <div class="head"><i></i><b>£425</b><i></i></div>
    <ul>
      <li><svg width="9" height="8" viewBox="0 0 9 8"><path d="M1 4l2.5 2.5L8 1" stroke="#6cb31e" stroke-width="1.8" fill="none"/></svg>4 Entertainers</li>
      <li><svg width="9" height="8" viewBox="0 0 9 8"><path d="M1 4l2.5 2.5L8 1" stroke="#6cb31e" stroke-width="1.8" fill="none"/></svg>40 childrens</li>
      <li><svg width="9" height="8" viewBox="0 0 9 8"><path d="M1 4l2.5 2.5L8 1" stroke="#6cb31e" stroke-width="1.8" fill="none"/></svg>40 Party bags</li>
      <li><svg width="9" height="8" viewBox="0 0 9 8"><path d="M1 4l2.5 2.5L8 1" stroke="#6cb31e" stroke-width="1.8" fill="none"/></svg>40 Spy ID's</li>
      <li><svg width="9" height="8" viewBox="0 0 9 8"><path d="M1 4l2.5 2.5L8 1" stroke="#6cb31e" stroke-width="1.8" fill="none"/></svg>2 Hours + Fun guarnateed</li>
    </ul>
    <div class="order slab">Order Now</div>
  </div>
</section>

<section class="abs share">
  <h2><b>Share</b> <span class="script">this on</span></h2>
  <div class="soc" style="left:134px">Chatterly</div>
  <div class="soc on" style="left:197px">Flockit</div>
  <div class="soc" style="left:263px">Reelo</div>
  <div class="soc" style="left:329px">Circlo</div>
  <div class="soc" style="left:395px">
    <svg width="18" height="18" viewBox="0 0 18 18"><circle cx="3" cy="15" r="2.2" fill="#6cb31e"/><path d="M1 8a9 9 0 0 1 9 9M1 2a15 15 0 0 1 15 15" stroke="#6cb31e" stroke-width="2.6" fill="none"/></svg>
  </div>
</section>

<div class="abs top-btn"><svg width="12" height="18" viewBox="0 0 12 18"><path d="M6 17V2M1 7l5-5 5 5" stroke="#fff" stroke-width="1.6" fill="none"/></svg></div>

<footer>
  <section class="abs band">
    <h3 class="slab">Is this a great party?</h3>
    <p>Many of our bookings come through recommendation. We have previous clients that would be happy to share their experience of a Spy Birthday Party; if you would like to talk to them let us know. You can also see some of our client feed-</p>
    <div class="agent" role="img" aria-label="Illustration of a detective in a trench coat and hat"></div>
    <div class="suit slab">SUITABLE FOR Boys<br>or Girls Age 6-12 years</div>
  </section>
  <nav class="abs foot-nav slab"><span>HOME</span><span>EQUIPMENT</span><span>INVITATIONS</span><span>PARTY</span><span>BAGS</span><span>PRICES</span><span>CONTACT</span></nav>
  <div class="abs copy">Copyright © 2011-2013 Fen-rally Ltd.</div>
</footer>

</body>
</html>
```